Design the Business card for VaultPeak

Business card required for a professional Cyber Security business.
Company Logo and Icon has already been provided however I would like other options for the logo and icon to compare to. Alternatively, please refine/enhance the image of the logo.icon I have already provided.

If you are going to use the provided logo and icon, I was thinking that the company raised Logo on White background would serve well on the front of the card. See attached. AND, a large company raised stand-alone icon to appear on black background on the back of the card with tagline 'Cyber Risk Management, Governance and Consulting' or 'Cyber Security for your Business' See attached.
Alternatively, provide your own design for the logo and icon.

Target Market(s)

Enterprise, Government, Financial.

Contact Information for Business Card

Teodor Halvik
Founder and CEO

Email Address
Mobile Number
Website URL
LinkedIn URL

Logo Text

VaultPeak - see attached example of logo

Font styles to use
Other font styles liked:
• Berlin Sans FB

Requirements
Must have
• Clean large and bold icon on the back with tagline.
• Horizontal alignment,
Nice to have
• Round edges.
• Raised Logo/Icon
Should not have
• An unprofessional look and feel.

```html
<!DOCTYPE html>
<html lang="en">
<head>
<meta charset="utf-8">
<title>VaultPeak Business Card</title>
<link href="https://fonts.googleapis.com/css2?family=Lato:wght@400;700;900&display=swap" rel="stylesheet">
<style>
  :root {
    --bg: #2a2a2a;
    --card: #030303;
    --blue: #2c7fc4;
    --mark-blue: #4f77c2;
    --yellow: #f4bd1a;
    --white: #f5f5f5;
    --divider: #5a5a5a;
  }
  * { margin: 0; padding: 0; box-sizing: border-box; }
  html, body { width: 1200px; height: 900px; overflow: hidden; }
  body {
    background: var(--bg);
    font-family: "Lato", Arial, sans-serif;
    position: relative;
  }
  .card {
    position: absolute;
    width: 640px;
    height: 366px;
    background: var(--card);
    border-radius: 16px;
    border-bottom: 5px solid var(--yellow);
    overflow: hidden;
    box-shadow: 0 18px 40px rgba(0,0,0,.55);
  }
  .card--front { left: 60px; top: 60px; }
  .card--back { left: 500px; top: 474px; }

  /* front */
  .brand {
    position: absolute;
    left: 0; right: 0; top: 130px;
    display: flex; align-items: center; justify-content: center; gap: 18px;
  }
  .brand__dot {
    width: 58px; height: 58px; border-radius: 50%;
    background: var(--mark-blue);
  }
  .brand__name {
    font-weight: 700; font-size: 62px; color: var(--blue); letter-spacing: 1px;
  }
  .tagline {
    position: absolute; left: 0; right: 0; bottom: 70px;
    text-align: center; color: var(--white);
    font-size: 15px; letter-spacing: 3px;
  }

  /* back */
  .mark {
    position: absolute; left: 40px; top: 90px; width: 220px;
    display: flex; flex-direction: column; align-items: center; gap: 14px;
  }
  .mark__dot {
    width: 130px; height: 130px; border-radius: 50%; background: var(--mark-blue);
  }
  .mark__name { font-weight: 700; font-size: 28px; color: var(--blue); }
  .divider {
    position: absolute; left: 290px; top: 70px; width: 2px; height: 230px;
    background: var(--divider);
  }
  .contact { position: absolute; left: 320px; top: 88px; }
  .person__name {
    font-weight: 900; font-size: 24px; letter-spacing: .5px; text-transform: uppercase;
  }
  .person__first { color: var(--blue); }
  .person__last { color: var(--yellow); }
  .person__role { color: var(--white); font-weight: 700; font-size: 15px; margin-top: 2px; }
  .details { list-style: none; margin-top: 30px; }
  .details li {
    display: flex; align-items: center; gap: 12px;
    color: var(--white); font-size: 16px; margin-bottom: 9px;
  }
  .icon {
    width: 24px; height: 24px; border-radius: 50%; background: var(--yellow);
    display: flex; align-items: center; justify-content: center; flex: none;
  }
  .icon svg { width: 14px; height: 14px; }
</style>
</head>
<body>
  <section class="card card--front">
    <div class="brand">
      <span class="brand__dot"></span>
      <span class="brand__name">VaultPeak</span>
    </div>
    <p class="tagline">Cyber Security for your Business</p>
  </section>

  <section class="card card--back">
    <div class="mark">
      <span class="mark__dot"></span>
      <span class="mark__name">VaultPeak</span>
    </div>
    <div class="divider"></div>
    <div class="contact">
      <h1 class="person__name"><span class="person__first">Teodor</span> <span class="person__last">Halvik</span></h1>
      <p class="person__role">Founder and CEO</p>
      <ul class="details">
        <li><span class="icon"><svg viewBox="0 0 16 16"><path d="M3 2h3l1 3-2 1a8 8 0 0 0 5 5l1-2 3 1v3a1 1 0 0 1-1 1A12 12 0 0 1 2 3a1 1 0 0 1 1-1z" fill="#000"/></svg></span>512.555.0199</li>
        <li><span class="icon"><svg viewBox="0 0 16 16"><rect x="2" y="4" width="12" height="8" fill="#000"/><path d="M2 4l6 5 6-5" stroke="#f4bd1a" stroke-width="1.2" fill="none"/></svg></span>teodor@vaultpeak.com</li>
        <li><span class="icon"></span>linkedin.com/teodorhalvik</li>
        <li><span class="icon"><svg viewBox="0 0 16 16"><circle cx="8" cy="8" r="6" stroke="#000" stroke-width="1.5" fill="none"/><ellipse cx="8" cy="8" rx="2.5" ry="6" stroke="#000" stroke-width="1.2" fill="none"/><path d="M2 8h12" stroke="#000" stroke-width="1.2"/></svg></span>www.vaultpeak.com</li>
      </ul>
    </div>
  </section>
</body>
</html>
```